KRT-VB 2018 Recycling Rate Report

We need a design for our 2018 Recycling Rate Report on Expanded Polystyrene. We want to move from a larger booklet style to a two page document. The report from last year - which was done as a booklet - is attached to provide an example of our style and design.The primary items that must be included (but not limited to) the information on pages 3, 5 & 7. The graphs must include room for 2018 data.To view our typical company design/style please see our website at www.kortavale.org. Our primary RGB colors are: (187,140,9); (94,47,29); (94,138,164); and (164,167,15). Secondary RGB colors are (249,162,28) and (218,210,208). Our title/header font is DIN Next LT Pro and our copy font is Calibri 10.5 pt. We can deviate from the font specification if beneficial and welcome interesting text treatments and typography.

Target Market(s)

Recycling facilities & general public.

Font styles to use
Sans Serif

Requirements
Must have
• Information presentation must be clean and easy to reference.

```html
<!DOCTYPE html>
<html lang="en">
<head>
<meta charset="utf-8">
<title>KRT-VB 2018 EPS Recycling Rate Report</title>
<link rel="stylesheet" href="https://fonts.googleapis.com/css2?family=Barlow:wght@400;500;600;700&family=Carlito:wght@400;700&display=swap">
<style>
  :root{
    --gold:#bb8c09;
    --brown:#5e2f1d;
    --steel:#5e8aa4;
    --olive:#a4a70f;
    --orange:#f9a21c;
    --stone:#dad2d0;
    --stone-light:#e3dcda;
    --ink:#222;
    --canvas:#ececec;
    --grid:#d8d8d8;
  }
  *{margin:0;padding:0;box-sizing:border-box}
  html,body{width:1200px;height:1000px;overflow:hidden;background:var(--canvas)}
  body{position:relative;font-family:"Carlito",Calibri,sans-serif;color:var(--ink)}
  .page{position:absolute;top:150px;width:496px;height:702px;background:#fff;overflow:hidden}
  .page--cover{left:78px}
  .page--data{left:636px;width:494px}
  .abs{position:absolute}
  svg{position:absolute;overflow:visible}

  /* cover */
  .cover-photo{position:absolute;inset:0;background:radial-gradient(ellipse at 30% 20%,#fafafa 0%,#e9e9e9 45%,#dedede 100%)}
  .title-panel{position:absolute;left:219px;top:53px;width:250px;height:649px;background:#fff}
  .kicker{position:absolute;left:12px;top:12px;font-family:"Barlow",sans-serif;color:var(--olive);font-size:27px;line-height:28px;font-weight:400;letter-spacing:.3px}
  .kicker strong{display:block;font-weight:700;font-size:29px}
  .year-block{position:absolute;left:11px;top:74px;width:228px;height:103px;background:var(--olive);color:#fff;font-family:"Barlow",sans-serif;font-size:96px;line-height:103px;text-align:center;font-weight:400}
  .report-band{position:absolute;left:11px;top:177px;width:228px;height:28px;background:var(--gold);color:#fff;font-family:"Barlow",sans-serif;font-size:15.5px;line-height:28px;text-align:center;letter-spacing:.4px}
  .copy-panel{position:absolute;left:11px;top:217px;width:228px;height:420px;background:var(--stone-light);padding:10px 9px}
  .copy-panel h2{font-family:"Barlow",sans-serif;font-weight:600;font-size:15px;line-height:15px;margin:0 0 4px;color:#111}
  .copy-panel p{font-size:8.1px;line-height:10.4px;margin-bottom:9px}
  .copy-panel h2.second{margin-top:14px}
  .brand{position:absolute;left:30px;top:612px;display:flex;align-items:center;gap:7px}
  .brand-dot{width:50px;height:50px;border-radius:50%;background:var(--gold)}
  .brand-name{font-family:"Barlow",sans-serif;color:var(--gold);font-size:14px;line-height:15px;font-weight:500}

  /* data page */
  .stat-band{position:absolute;left:26px;top:16px;width:298px;height:132px;background:var(--stone)}
  .photo{position:absolute;top:0;height:70px;width:123px}
  .photo--industrial{left:2px;background:linear-gradient(135deg,#6d6d6d,#c9c9c9 60%,#8a8a8a)}
  .photo--consumer{left:151px;background:linear-gradient(135deg,#7b7b7b,#e4e4e4 55%,#9c9c9c)}
  .stat{position:absolute;top:74px;width:140px;text-align:center}
  .stat--industrial{left:-6px}
  .stat--consumer{left:143px}
  .stat-label{font-size:15px;line-height:15px;color:#222}
  .stat-unit{font-size:5.5px;line-height:7px;color:#444}
  .stat-value{font-family:"Barlow",sans-serif;font-weight:700;font-size:24px;line-height:24px}
  .stat--industrial .stat-value{color:var(--orange)}
  .stat--consumer .stat-value{color:var(--olive)}
  .side-note{position:absolute;left:336px;width:136px;font-size:8.1px;line-height:10.2px}
  .side-note--top{top:32px}
  .side-note--data{top:358px}
  .chart-bar{position:absolute;left:26px;width:443px;height:17px;color:#fff;font-family:"Barlow",sans-serif;font-weight:700;font-size:10.5px;line-height:17px;text-align:center}
  .chart-bar--olive{top:155px;background:var(--olive)}
  .chart-bar--steel{top:504px;background:var(--steel)}
  .rule{position:absolute;left:26px;top:340px;width:443px;height:1px;background:#cfcfcf}
  .data-tab{position:absolute;left:26px;top:350px;width:90px;height:23px;font-family:"Barlow",sans-serif;font-weight:700;color:var(--steel);font-size:17px;line-height:23px;padding-left:2px}
  .data-box{position:absolute;left:26px;top:373px;width:286px;height:117px;background:var(--steel);color:#fff}
  .data-box p{position:absolute;left:3px;top:7px;width:178px;font-size:7.9px;line-height:10.1px}
  .data-photo{position:absolute;left:207px;top:353px;width:102px;height:66px;background:linear-gradient(160deg,#f2f2f2,#cfcfcf)}
  .total{position:absolute;left:188px;top:421px;width:124px;text-align:center;color:#fff}
  .total-label{font-size:11px;line-height:12px}
  .total-unit{font-size:5.5px;line-height:7px}
  .total-value{font-family:"Barlow",sans-serif;font-weight:700;font-size:27px;line-height:30px}
  .bar-unit{position:absolute;left:26px;top:526px;width:443px;text-align:center;font-size:6.5px}
  .legend{position:absolute;left:30px;top:546px;display:flex;gap:18px;font-size:6px;align-items:center}
  .legend span{display:flex;align-items:center;gap:8px}
  .legend i{display:block;width:14px;height:14px;border-radius:50%}
  .legend .lg-consumer i{background:var(--olive)}
  .legend .lg-industrial i{background:var(--orange)}
  .axis-text{font-family:"Carlito",sans-serif;font-size:6px;fill:#333}
  .val-text{font-family:"Carlito",sans-serif;font-size:6.5px;fill:#444}
</style>
</head>
<body>

<section class="page page--cover">
  <div class="cover-photo" role="img" aria-label="Close-up photograph of white expanded polystyrene beads"></div>
  <div class="title-panel">
    <h1 class="kicker">TAKE A LOOK AT<strong>EPS RECYCLING</strong></h1>
    <div class="year-block">2018</div>
    <div class="report-band">EPS RECYCLING RATE REPORT</div>
    <div class="copy-panel">
      <h2>METHODOLOGY</h2>
      <p>The 2017 Expanded Polystyrene Recycling Rate Study was conducted by the Kortavale Alliance to gather data to reflect both post-consumer and post-industrial recycling activity. The 2017 results are based on data received from 55 EPS manufacturers and independent recyclers in the U.S.</p>
      <p>Participation in the EPS recycling survey is voluntary and the reported data is based on the responses received. Many companies have limited resources to put towards participation in the survey, and some companies may choose not to respond due to their confidentiality policies. Therefore, because there is not 100 percent participation, the presented totals represent the minimum amount of EPS recovered for recycling.</p>
      <h2 class="second">COLLECTION OPTIONS<br>&amp; RESOURCES</h2>
      <p>Not everything can be recycled all the time. In order for materials to be recycled, stable markets must exist and there must be a demand for the end products. Each community has its own guidelines for which plastics are accepted, and these can vary widely. Some locations also offer consumer dropoff access. To find out if EPS recycling is available in your area, visit www.kortavale.org.</p>
      <p>For consumers that do not have access to a local drop-off center, the KRT-VB sponsors a National Mail-Back Program intended for smaller quantities of EPS which can be mailed via NatPost or ParcelWay to more than 20 locations nationwide. Full instructions and a list of Mail-Back locations are available on the KRT-VB website.</p>
    </div>
  </div>
  <div class="brand">
    <div class="brand-dot"></div>
    <div class="brand-name">Kortavale<br>Alliance</div>
  </div>
</section>

<section class="page page--data">
  <div class="stat-band">
    <div class="photo photo--industrial" role="img" aria-label="Photograph of stacked post-industrial EPS scrap"></div>
    <div class="photo photo--consumer" role="img" aria-label="Photograph of a worker handling a post-consumer EPS sheet"></div>
    <div class="stat stat--industrial">
      <div class="stat-label">Post-Industrial</div>
      <div class="stat-unit">(millions of pounds)</div>
      <div class="stat-value">39.0</div>
    </div>
    <div class="stat stat--consumer">
      <div class="stat-label">Post-Consumer</div>
      <div class="stat-unit">(millions of pounds)</div>
      <div class="stat-value">25.9</div>
    </div>
  </div>
  <p class="side-note side-note--top">The 25-year baseline shows incremental gains with more than 23 million pounds of EPS recycled annually on average. Like all commodity markets, the EPS recycling market is cyclical. The 2017 results reflect a decrease from 2016 due to the new landscape for recycling commodities and chaning international markets, especially in China.</p>

  <div class="chart-bar chart-bar--olive">Post-Consumer EPS Recycling 1990-2018</div>
  <svg style="left:26px;top:180px" width="443" height="155" viewBox="662 330 443 155">
    <g stroke="var(--grid)" stroke-width="0.8">
      <line x1="690" y1="336" x2="690" y2="470"/>
      <line x1="719" y1="336" x2="719" y2="470"/><line x1="750" y1="336" x2="750" y2="470"/>
      <line x1="779" y1="336" x2="779" y2="470"/><line x1="806" y1="336" x2="806" y2="470"/>
      <line x1="834" y1="336" x2="834" y2="470"/><line x1="862" y1="336" x2="862" y2="470"/>
      <line x1="890" y1="336" x2="890" y2="470"/><line x1="918" y1="336" x2="918" y2="470"/>
      <line x1="945" y1="336" x2="945" y2="470"/><line x1="973" y1="336" x2="973" y2="470"/>
      <line x1="1000" y1="336" x2="1000" y2="470"/><line x1="1026" y1="336" x2="1026" y2="470"/>
      <line x1="1051" y1="336" x2="1051" y2="470"/><line x1="1077" y1="336" x2="1077" y2="470"/>
      <line x1="1104" y1="336" x2="1104" y2="470"/>
      <line x1="690" y1="470" x2="1104" y2="470" stroke="#bbb"/>
    </g>
    <text class="axis-text" transform="translate(670 403) rotate(-90)" text-anchor="middle" fill="var(--olive)" style="fill:var(--olive)">Millions of Pounds Recycled</text>
    <g class="axis-text" text-anchor="end">
      <text x="686" y="472">0</text><text x="686" y="453.4">10</text><text x="686" y="434.9">20</text>
      <text x="686" y="416.3">30</text><text x="686" y="397.7">40</text><text x="686" y="379.1">50</text>
      <text x="686" y="360.6">60</text><text x="686" y="342">70</text>
    </g>
    <polyline fill="none" stroke="var(--olive)" stroke-width="1.3"
      points="705,464.4 734,431.4 765,425.1 793,428.2 820,436.2 848,423.8 876,421.3 904,423.6 931,410.6 959,407.6 987,401.1 1013,401.8 1039,353 1063,421.9"/>
    <g fill="var(--olive)">
      <circle cx="705" cy="464.4" r="2.2"/><circle cx="734" cy="431.4" r="2.2"/><circle cx="765" cy="425.1" r="2.2"/>
      <circle cx="793" cy="428.2" r="2.2"/><circle cx="820" cy="436.2" r="2.2"/><circle cx="848" cy="423.8" r="2.2"/>
      <circle cx="876" cy="421.3" r="2.2"/><circle cx="904" cy="423.6" r="2.2"/><circle cx="931" cy="410.6" r="2.2"/>
      <circle cx="959" cy="407.6" r="2.2"/><circle cx="987" cy="401.1" r="2.2"/><circle cx="1013" cy="401.8" r="2.2"/>
      <circle cx="1039" cy="353" r="2.2"/><circle cx="1063" cy="421.9" r="2.2"/>
    </g>
    <g class="val-text" text-anchor="middle">
      <text x="705" y="458">3.0</text><text x="734" y="425">20.8</text><text x="765" y="418.5">24.2</text>
      <text x="793" y="421.5">22.5</text><text x="820" y="429.5">18.2</text><text x="848" y="417">24.9</text>
      <text x="876" y="414.5">26.2</text><text x="904" y="417">25.0</text><text x="931" y="404">32.0</text>
      <text x="959" y="401">33.6</text><text x="987" y="394.5">37.1</text><text x="1013" y="395">36.7</text>
      <text x="1039" y="346.5">63.0</text><text x="1063" y="432">25.9</text>
    </g>
    <g class="axis-text" text-anchor="middle">
      <text x="705" y="479">1990</text><text x="734" y="479">1992</text><text x="765" y="479">1994</text>
      <text x="793" y="479">1996</text><text x="820" y="479">1998</text><text x="848" y="479">2000</text>
      <text x="876" y="479">2002</text><text x="904" y="479">2004</text><text x="931" y="479">2006</text>
      <text x="959" y="479">2008</text><text x="987" y="479">2010</text><text x="1013" y="479">2012</text>
      <text x="1039" y="479">2016</text><text x="1063" y="479">2017</text><text x="1091" y="479">2018</text>
    </g>
  </svg>

  <div class="rule"></div>
  <div class="data-tab">DATA</div>
  <div class="data-box">
    <p>More than 65 million pounds of EPS were recycled during calendar year 2017. This figure includes 25.9 million pounds of post-consumer packaging and 39.0 million pounds of post-industrial recovery. Post-consumer is defined as any material that is recycled after its intended end-use while post-industrial recovery includes EPS facility scrap that is recycled but never served its intended purpose as a packaging material or other end-use application.</p>
  </div>
  <div class="data-photo" role="img" aria-label="Photograph of a recycling code moulded into white EPS"></div>
  <div class="total">
    <div class="total-label">2017 Total</div>
    <div class="total-unit">million pounds of EPS recycled</div>
    <div class="total-value">65.0</div>
  </div>
  <p class="side-note side-note--data">Despite lower collection amounts reflected in 2017, EPS has historically enjoyed consistent growth since its inception in the early 1990's. This decrease is a direct result of export restrictions on recycled plastics and a reprocessing plant closure that previously recycled large quantities of EPS. Newer EPS recycling technologies to facilitate EPS collection and reprocessing launched in 2018 indicate growth rates will continue on an upward trend in the future.</p>

  <div class="chart-bar chart-bar--steel">EPS Recycling Post-Consumer &amp; Post-Industrial</div>
  <div class="bar-unit">(millions of pounds)</div>
  <div class="legend">
    <span class="lg-consumer"><i></i>POST-CONSUMER</span>
    <span class="lg-industrial"><i></i>POST-INDUSTRIAL</span>
  </div>
  <svg style="left:26px;top:535px" width="443" height="150" viewBox="662 685 443 150">
    <g fill="var(--olive)">
      <rect x="665" y="771.7" width="23" height="48.3"/><rect x="730" y="771.5" width="23" height="48.5"/>
      <rect x="793" y="754.8" width="23" height="65.2"/><rect x="860" y="748.8" width="23" height="71.2"/>
      <rect x="925" y="697.8" width="23" height="122.2"/><rect x="990" y="769.8" width="23" height="50.2"/>
    </g>
    <g fill="var(--orange)">
      <rect x="692" y="789.7" width="23" height="30.3"/><rect x="755" y="756.2" width="23" height="63.8"/>
      <rect x="818" y="750.5" width="23" height="69.5"/><rect x="885" y="709.6" width="23" height="110.4"/>
      <rect x="950" y="711.9" width="23" height="108.1"/><rect x="1015" y="744.3" width="23" height="75.7"/>
    </g>
    <line x1="662" y1="820" x2="1105" y2="820" stroke="#bbb" stroke-width="0.8"/>
    <g class="val-text" text-anchor="middle" style="fill:var(--olive)">
      <text x="676.5" y="768">24.9</text><text x="741.5" y="768">25.0</text><text x="804.5" y="751">33.6</text>
      <text x="871.5" y="745">36.7</text><text x="936.5" y="694">63.0</text><text x="1001.5" y="766">25.9</text>
    </g>
    <g class="val-text" text-anchor="middle" style="fill:var(--orange)">
      <text x="703.5" y="786">15.6</text><text x="766.5" y="752.5">32.9</text><text x="829.5" y="747">35.8</text>
      <text x="896.5" y="706">56.9</text><text x="961.5" y="708">55.7</text><text x="1026.5" y="740.5">39.0</text>
    </g>
    <g class="axis-text" text-anchor="middle">
      <text x="690" y="831">2000</text><text x="754" y="831">2004</text><text x="817" y="831">2008</text>
      <text x="884" y="831">2012</text><text x="949" y="831">2016</text><text x="1014" y="831">2017</text>
      <text x="1080" y="831">2018</text>
    </g>
  </svg>
</section>

</body>
</html>
```